R J Penn Accounting & SMSF Auditing needs a Web Site Design

I need some examples of what a web design can look like for my business.
The business name is above and I have already registered a domain name of www.penn-smsf.com.au
I have attached my current letterhead and business cards and would like to maintain these colours basically Red on White with some black

Industry/Entity Type

Business

```html
<!DOCTYPE html>
<html lang="en">
<head>
<meta charset="utf-8">
<title>R J Penn Accounting &amp; SMSF Auditing</title>
<link href="https://fonts.googleapis.com/css2?family=Oswald:wght@400;500&family=Libre+Baskerville:wght@700&family=Arimo:wght@400&display=swap" rel="stylesheet">
<style>
:root{
  --red:#c4000f;
  --red-dark:#9c0a12;
  --ink:#333;
  --grey:#555;
  --topbar:#1c1c1c;
  --navband:#f2f2f2;
  --line:#ddd;
}
*{box-sizing:border-box;margin:0;padding:0}
html,body{width:1200px;height:900px;overflow:hidden;background:#fff;font-family:Arimo,Arial,sans-serif;color:var(--ink)}
.page{position:relative;width:1200px;height:900px}
.topbar{position:absolute;left:0;top:0;width:1200px;height:36px;background:var(--topbar);font-size:11px;color:var(--red)}
.topbar .item{position:absolute;top:11px;display:flex;align-items:center;gap:9px}
.topbar svg{flex:none}
.navband{position:absolute;left:0;top:36px;width:1200px;height:56px;background:var(--navband)}
.nav{position:absolute;top:53px;left:473px;display:flex;font-size:13px;color:var(--grey)}
.nav a{color:inherit;text-decoration:none;text-transform:uppercase}
.nav a.active{background:#fff;color:var(--red);padding:4px 18px;height:23px}
.brand{position:absolute;left:123px;top:36px;width:301px;height:86px;background:#fff;border-bottom:1px solid #555;padding:18px 0 0 11px}
.brand .name{font-family:"Libre Baskerville",Georgia,serif;font-weight:700;font-size:31px;color:var(--red);letter-spacing:.5px;line-height:1}
.brand .tag{font-family:"Libre Baskerville",Georgia,serif;font-weight:700;font-size:12.5px;color:#222;margin-top:7px;letter-spacing:.3px}
.hero{position:absolute;left:0;top:92px;width:1200px;height:465px;background:radial-gradient(ellipse at 70% 35%,#e9a55c 0%,#b46a2c 35%,#6b3414 70%,#2e1608 100%)}
.hero-caption{position:absolute;left:123px;top:208px;width:422px;height:180px;background:rgba(40,22,12,.7);padding:42px 0 0 22px;font-family:Oswald,sans-serif;font-weight:500;font-size:38px;line-height:47px;color:#fff}
.features{position:absolute;left:0;top:557px;width:1200px;height:178px;background:linear-gradient(#f9f9f9,#f1f1f1);border-top:1px dashed #ccc}
.book{position:absolute;left:155px;top:562px;width:146px;height:158px;background:linear-gradient(135deg,#3a3a3a,#111 60%,#6b2b16);border-radius:4px}
.feature{position:absolute;top:557px;width:241px;height:178px;padding:24px 14px 0 14px}
.feature h3{font-family:Oswald,sans-serif;font-weight:500;font-size:25px;color:#444;text-align:center;margin-bottom:16px}
.feature p{font-size:14px;line-height:22px;color:var(--grey);text-align:justify}
.feature .go{position:absolute;right:14px;bottom:10px}
.feature.current{background:linear-gradient(#fdfdfd,#e9e9e9);border-left:1px solid var(--line);border-right:1px solid var(--line)}
.feature.current h3{color:var(--red)}
.notch{position:absolute;left:711px;top:557px}
.redline{position:absolute;left:0;top:735px;width:1200px;height:5px;background:var(--red-dark)}
.services{position:absolute;left:117px;top:721px;width:244px;height:179px;background:#fff}
.services h2{height:52px;background:linear-gradient(var(--red),var(--red-dark));border-left:4px solid #6d0008;color:#fff;font-family:Oswald,sans-serif;font-weight:500;font-size:19px;padding:13px 0 0 23px}
.services ul{list-style:none;padding:0 16px 0 18px;font-size:14px}
.services li{position:relative;padding:10px 0 7px 18px;border-bottom:1px solid #e2e2e2}
.services li::before{content:"›";position:absolute;left:0;top:6px;color:var(--red);font-size:18px}
.services li.active{color:var(--red);padding-left:41px;padding-top:11px;border-bottom:1px solid var(--red)}
.content{position:absolute;left:376px;top:767px;width:450px}
.content h2{border-top:1px solid var(--line);border-bottom:1px solid var(--line);padding:4px 5px;font-family:Oswald,sans-serif;font-weight:500;font-size:25px;color:var(--red)}
.content p{padding:22px 10px 0 9px;font-size:14px;line-height:22px;color:var(--grey);text-align:justify}
.side{position:absolute;left:849px;top:769px;width:221px}
.promo{display:flex;height:76px;margin-bottom:11px}
.promo .photo{width:80px;background:linear-gradient(135deg,#b9a06a,#5c4a2c)}
.promo .label{flex:1;background:var(--red);color:#fff;padding:12px 0 0 20px;font-family:"Libre Baskerville",Georgia,serif;font-weight:700;font-size:14px}
.promo .label b{display:block;font-family:Oswald,sans-serif;font-weight:500;font-size:30px;line-height:34px}
.promo.dark .photo{background:linear-gradient(135deg,#999,#333)}
.promo.dark .label{background:#3b3b3b}
.rightstrip{position:absolute;left:1077px;top:740px;width:123px;height:160px;background:#ececec}
</style>
</head>
<body>
<div class="page">
  <header class="topbar">
    <div class="item" style="left:589px">
      <svg width="20" height="20" viewBox="0 0 20 20" fill="none" stroke="#fff" stroke-width="1.3"><circle cx="10" cy="10" r="8.5"/><ellipse cx="10" cy="10" rx="3.8" ry="8.5"/><path d="M1.5 10h17M3 5.5h14M3 14.5h14"/></svg>
      <span>PO Box 118 Riverton WA 6148</span>
    </div>
    <div class="item" style="left:833px">
      <svg width="19" height="12" viewBox="0 0 19 12" fill="#fff"><path d="M0 0h19v12H0z"/><path d="M0 0l9.5 7L19 0" fill="none" stroke="#333"/></svg>
      <span>rjpenn@webmail.net.au</span>
    </div>
    <div class="item" style="left:1021px">
      <svg width="20" height="13" viewBox="0 0 20 13" fill="#fff"><path d="M0 4c2-4 18-4 20 0v2h-5V4H5v2H0z"/><rect x="3" y="6" width="14" height="7" rx="1"/></svg>
      <span>704 555 0199</span>
    </div>
  </header>
  <div class="navband"></div>
  <nav class="nav">
    <a class="active" href="#">Home</a>
    <a href="#" style="margin:4px 0 0 75px">About</a>
    <a href="#" style="margin:4px 0 0 84px">Services</a>
    <a href="#" style="margin:4px 0 0 80px">Case Study</a>
    <a href="#" style="margin:4px 0 0 80px">Contact</a>
  </nav>
  <div class="brand">
    <div class="name">R J PENN</div>
    <div class="tag">ACCOUNTING &amp; SMSF AUDITING</div>
  </div>

  <section class="hero" role="img" aria-label="Brass scales of justice on a wooden desk before blurred law library shelves"></section>
  <div class="hero-caption">We offer our clients only<br>expert legal advice</div>

  <div class="features"></div>
  <div class="book" role="img" aria-label="Black law book with a wooden gavel"></div>
  <svg class="notch" width="18" height="9" viewBox="0 0 18 9"><path d="M0 0h18L9 9z" fill="#a8141c"/></svg>

  <div class="feature" style="left:354px">
    <h3>Find a Lawyer</h3>
    <p>Lorem Ipsum is simply dummy text of and industry. Lorem has been the industry's.</p>
    <svg class="go" width="17" height="17" viewBox="0 0 17 17"><circle cx="8.5" cy="8.5" r="7.5" fill="#fff" stroke="#c4000f" stroke-width="1.3"/><path d="M6.5 5l4 3.5-4 3.5z" fill="#c4000f"/></svg>
  </div>
  <div class="feature current" style="left:599px">
    <h3>Our Company</h3>
    <p>Lorem Ipsum is simply dummy text of and industry. Lorem has been the industry's.</p>
    <svg class="go" width="17" height="17" viewBox="0 0 17 17"><circle cx="8.5" cy="8.5" r="7.5" fill="#f0b070" stroke="#9a4a00" stroke-width="1.3"/><path d="M6.5 5l4 3.5-4 3.5z" fill="#9a2000"/></svg>
  </div>
  <div class="feature" style="left:840px">
    <h3>Case Study</h3>
    <p>Lorem Ipsum is simply dummy text of and industry. Lorem has been the industry's.</p>
    <svg class="go" width="17" height="17" viewBox="0 0 17 17"><circle cx="8.5" cy="8.5" r="7.5" fill="#fff" stroke="#c4000f" stroke-width="1.3"/><path d="M6.5 5l4 3.5-4 3.5z" fill="#c4000f"/></svg>
  </div>

  <div class="redline"></div>
  <div class="rightstrip"></div>

  <aside class="services">
    <h2>OUR SERVICES</h2>
    <ul>
      <li>Business Licensing</li>
      <li>Self Protection</li>
      <li class="active">Business Licensing</li>
      <li>Justice Center</li>
    </ul>
  </aside>

  <main class="content">
    <h2>Why Choose R J Penn</h2>
    <p>Lorem Ipsum is simply dummy text of and industry. Lorem has been the 1500s, when an unknown printer took a galley of type and scram-bled it to make a type specimen book.</p>
  </main>

  <aside class="side">
    <div class="promo">
      <div class="photo" role="img" aria-label="Courthouse columns with a pointing hand cursor"></div>
      <div class="label">CHAT WITH US<b>Online</b></div>
    </div>
    <div class="promo dark">
      <div class="photo" role="img" aria-label="Bankruptcy documents"></div>
      <div class="label">BANKRUPTCY<b>FAQ</b></div>
    </div>
  </aside>
</div>
</body>
</html>
```